CD front and back cover and CD disk. Front includes design elements of the attached band photo, the name of the band (Quiet Harbor Lanterns) and the album name (Paper Anchors?). I've attached a photshoped band photo and an original image. I like the color palette of the photoshoped pix but it may be too dark. So I've attached the original pix, that could be photoshoped. Music is alternative rock. See website qhlTunes.com and the EPK on the site. Songs are not up for this CD yet. Concept - modern, clean, NO gothic rock font or style of any kind.

Back cover needs songs, website and contact as follows:

Hold Ember (Electric)
Linger
Bent and Broken
Meridian
You Sink You Swim
Lean Past You
Hold Ember (Acoustic)
Room To Roam
The Tide
Push Too Far

qhlTunes.com
info@qhlTunes.com
- the actual cd needs the same as above
- use the DiscNook template Sleeve S240 

• Back cover needs the song titles, website, contact info and copyright as follows:
Hold Ember (electric)
Linger
Bent and Broken
Meridian
You Sink You Swim
Lean Past You
Hold Ember (acoustic)
Room To Roam
The Tide
Push Too Far

qhlTune.com
info@qhlTunes.com
Copyright © 2013 Quiet Harbor Lanterns | All Rights Reserved
Also - dimensions for CD Sleeve S240 on discnook.com
Also - CD disk to contain all of the above

```html
<!DOCTYPE html>
<html lang="en">
<head>
<meta charset="utf-8">
<title>Quiet Harbor Lanterns – Back Cover</title>
<link href="https://fonts.googleapis.com/css2?family=Tinos:wght@400;700&display=swap" rel="stylesheet">
<style>
  :root {
    --bg: #000000;
    --title: #a9a9a9;
    --text: #ffffff;
    --accent: #e0604c;
  }
  * { margin: 0; padding: 0; box-sizing: border-box; }
  html, body {
    width: 1200px;
    height: 934px;
    overflow: hidden;
    background: var(--bg);
  }
  .back-cover {
    position: relative;
    width: 1200px;
    height: 934px;
    background: var(--bg);
    font-family: "Tinos", "Times New Roman", serif;
    color: var(--text);
  }
  .band-name {
    position: absolute;
    top: 78px;
    left: 673px;
    transform: translateX(-50%);
    white-space: nowrap;
    font-size: 60px;
    font-weight: 400;
    color: var(--title);
  }
  .track-list {
    position: absolute;
    top: 208px;
    left: 477px;
    list-style: none;
    font-size: 36px;
    line-height: 47.6px;
  }
  .website {
    position: absolute;
    top: 718px;
    left: 586px;
    transform: translateX(-50%);
    white-space: nowrap;
    font-size: 50px;
    font-weight: 700;
    color: var(--accent);
  }
  .contact {
    position: absolute;
    top: 800px;
    left: 600px;
    transform: translateX(-50%);
    white-space: nowrap;
    font-size: 39px;
  }
  .copyright {
    position: absolute;
    top: 860px;
    left: 600px;
    transform: translateX(-50%) scaleX(0.82);
    white-space: nowrap;
    font-size: 36px;
  }
</style>
</head>
<body>
  <main class="back-cover">
    <h1 class="band-name">Quiet Harbor Lanterns</h1>
    <ol class="track-list">
      <li>Hold Ember (electric)</li>
      <li>Linger</li>
      <li>Bent and Broken</li>
      <li>Meridian</li>
      <li>You Sink You Swim</li>
      <li>Lean Past You</li>
      <li>Hold Ember (acoustic)</li>
      <li>Room To Roam</li>
      <li>The Tide</li>
      <li>Push Too Far</li>
    </ol>
    <p class="website">qhlTune.com</p>
    <p class="contact">info@qhlTunes.com</p>
    <p class="copyright">Copyright © 2013 Quiet Harbor Lanterns | All Rights Reserved</p>
  </main>
</body>
</html>
```